LumoPledge Crowdfunding Website 1st Page

I am looking to have a first page created for a new crowd funding website that knocks down the biggest hurdle that creative types and start ups face, legal costs. For creative projects and innovative products, we are providing intellectual property and certain other legal services wrapped into the project costs.

I am using a white label crowdfunding platform that that has a standard look and feel of most crowdfunding sites e.g. tiles with campaigns, listing of campaigns categories, create new campaign options, and donate to campaigns etc. The white label program is branded with the LumoPledge logo and colors. At present there is a front page that is just a place holder for someone at ArtHively's great design! What I need is an eye-catching first page that visually and through content optimizes the LumoPledge brand. (There should be space for content for those looking to raise money and those looking to donate to campaigns.)

www.fundvexora.com is, of course, the reigning King of crowdfunding. They have been so successful that they no longer have to entice people to launch campaigns there. (So they don't speak as much to those looking to raise money.) Unlike Fundvexora, of the challenges is that I have two customers I need to engage. The first is the potential crowdfund campaign owner who is looking to raise money. The second customer is the donor.

I am looking for a smart page from a marketing standpoint that also grabs you. One should feel the energy of "the crowd" when they look at the page.

Some information regarding the logo: The font is Kabel BK BT. The primary blue is R33, G121, B 159. Hex21799F and the primary greenis R179, G210, B54 Hex B3D236. The third file is a slight variation on the LP logo that you are free to use as well. (Unfortunately, I don't have all the color information for that one readily available.) If you need more files, please just let me know.

Industry/Entity Type

Marketing

Font styles to use
Other font styles liked:
• Kabel Bk BT or complimentary

Requirements
Must have
• Please use the slogan "Where the crowd meets great ideas".

```html
<!DOCTYPE html>
<html lang="en">
<head>
<meta charset="utf-8">
<title>LumoPledge – Where the crowd meets great ideas</title>
<link rel="stylesheet" href="https://fonts.googleapis.com/css2?family=Questrial&display=swap">
<style>
:root{
  --blue:#21799f;
  --blue-light:#3aa2d2;
  --green:#b3d236;
  --green-dark:#7ab51d;
  --card-green:#9dc93b;
  --orange:#f07d1a;
  --ink:#222;
  --grey-line:#cfcfcf;
  --panel:#f4f4f4;
  --footer:#3d3a3b;
  --white:#fff;
}
*{margin:0;padding:0;box-sizing:border-box}
html,body{width:1200px;height:927px;overflow:hidden;background:var(--white)}
body{position:relative;font-family:"Questrial",sans-serif;color:var(--ink)}

/* header */
.site-header{position:absolute;left:0;top:0;width:1200px;height:118px;background:linear-gradient(#fff 0%,#fff 60%,#ececec 100%);border-bottom:1px solid #dcdcdc}
.brand{position:absolute;left:165px;top:15px;width:140px;height:80px}
.brand-mark{position:absolute;left:50px;top:2px;width:52px;height:52px;border-radius:50%;background:var(--blue-light)}
.brand-name{position:absolute;left:0;top:55px;font-size:23px;color:var(--blue);letter-spacing:-.4px}
.nav-sep{position:absolute;top:15px;width:1px;height:82px;background:linear-gradient(transparent,#d0d0d0 20%,#d0d0d0 80%,transparent)}
.nav-item{position:absolute;top:40px;letter-spacing:-.3px}
.nav-item .title{display:block;font-size:18px;color:var(--blue);line-height:20px}
.nav-item .sub{display:block;font-size:13px;color:var(--ink);margin-top:5px}
.btn{position:absolute;border-radius:7px;color:var(--white);font-size:15px;text-align:center;line-height:34px}
.btn-login{left:751px;top:14px;width:108px;height:36px;background:linear-gradient(#45a6d6,#1f7bb0);border:1px solid #1b6c99}
.btn-signup{left:872px;top:14px;width:108px;height:36px;background:linear-gradient(#c4e04c,#9ac42c);border:1px solid #8cb726}
.search{position:absolute;left:753px;top:65px;width:226px;height:33px;border:1px solid #bbb;border-radius:7px;background:#fff;box-shadow:inset 0 1px 2px rgba(0,0,0,.15)}
.search svg{position:absolute;left:8px;top:9px}
.search span{position:absolute;left:31px;top:9px;font-size:11px;color:#777}

/* hero */
.hero{position:absolute;left:0;top:118px;width:1200px;height:322px;background:var(--blue)}
.hero-art{position:absolute;left:165px;top:8px;width:485px;height:308px;border-radius:40px;background:radial-gradient(ellipse at 55% 45%,#d7dde2 0%,#a9b6bf 45%,rgba(33,121,159,0) 75%)}
.hero-title{position:absolute;left:624px;top:42px;font-size:23px;font-weight:normal;letter-spacing:-.6px;color:var(--white);white-space:nowrap}
.hero-rule{position:absolute;left:626px;top:80px;width:354px;border-top:1px dotted #cfe3ec}
.hero-copy{position:absolute;left:667px;top:91px;width:320px;font-size:12px;line-height:17px;letter-spacing:-.35px;color:var(--white);white-space:nowrap}
.hero-copy p+p{margin-top:17px}
.btn-learn{left:663px;top:220px;width:84px;height:32px;line-height:30px;font-size:13px;background:linear-gradient(#c4e04c,#9ac42c);border:1px solid #d7ec83;border-radius:6px}

/* sidebar */
.sidebar{position:absolute;left:165px;top:446px;width:150px;height:423px;border:1px solid var(--grey-line);background:var(--white)}
.side-head{position:absolute;left:0;font-size:17px}
.side-head svg{position:absolute;left:16px;top:3px}
.side-head span{position:absolute;left:42px;white-space:nowrap}
.popular{top:9px;color:var(--green-dark)}
.featured{top:39px;color:var(--orange)}
.categories{top:74px;color:var(--blue)}
.cat-list{position:absolute;left:0;top:98px;width:148px;list-style:none}
.cat-list li{height:24px;line-height:24px;padding-left:39px;font-size:13px}
.cat-list li:nth-child(odd){background:var(--panel)}

/* projects */
.projects{position:absolute;left:324px;top:446px;width:655px;height:423px;border:1px solid var(--grey-line);background:var(--panel)}
.card{position:absolute;top:11px;width:209px;height:400px;border:2px solid var(--card-green);border-radius:8px;background:var(--white);overflow:hidden}
.card-icon{position:absolute;left:6px;top:7px;width:26px;height:26px;border-radius:50%;background:var(--blue-light)}
.card-title{position:absolute;left:39px;top:10px;font-size:18px;letter-spacing:-.3px;color:var(--green-dark);white-space:nowrap}
.card-by{position:absolute;left:10px;top:38px;font-size:13.5px;letter-spacing:-.3px;white-space:nowrap}
.card-photo{position:absolute;left:6px;top:65px;width:193px;height:141px;background:linear-gradient(135deg,#b1a79f,#958a81)}
.card-desc{position:absolute;left:7px;top:210px;width:195px;font-size:10px;line-height:18px;letter-spacing:-.25px;white-space:nowrap}
.card-pin{position:absolute;left:9px;top:290px}
.card-loc{position:absolute;left:29px;top:297px;font-size:10px;letter-spacing:-.2px}
.progress{position:absolute;left:4px;top:318px;width:199px;height:18px;background:#f2f2f2}
.progress-track{position:absolute;left:4px;top:7px;width:190px;height:8px;border-radius:4px;background:#cfd3cf}
.progress-fill{position:absolute;left:0;top:0;width:74%;height:8px;border-radius:4px;background:#79c52a}
.stat{position:absolute;top:343px;text-align:center;white-space:nowrap;letter-spacing:-.3px}
.stat b{display:block;font-weight:normal;font-size:16px}
.stat span{display:block;font-size:13px;margin-top:5px}
.stat-funded{left:2px;width:62px}
.stat-pledged{left:64px;width:74px}
.stat-days{left:137px;width:68px}

/* footer */
.site-footer{position:absolute;left:0;top:873px;width:1200px;height:54px;background:var(--footer);color:var(--white);font-size:11px;line-height:54px;text-align:center;letter-spacing:-.2px}
.site-footer a{color:var(--white);text-decoration:none;padding:0 6px}
.site-footer i{font-style:normal}
</style>
</head>
<body>

<header class="site-header">
  <div class="brand">
    <div class="brand-mark"></div>
    <div class="brand-name">LumoPledge</div>
  </div>
  <div class="nav-sep" style="left:340px"></div>
  <div class="nav-item" style="left:372px"><span class="title">Discover</span><span class="sub">great projects</span></div>
  <div class="nav-sep" style="left:475px"></div>
  <div class="nav-item" style="left:502px"><span class="title">Start</span><span class="sub">a project</span></div>
  <div class="nav-sep" style="left:579px"></div>
  <div class="nav-item" style="left:606px"><span class="title">How it works</span><span class="sub">learn more</span></div>
  <div class="nav-sep" style="left:723px"></div>
  <div class="btn btn-login">Log in</div>
  <div class="btn btn-signup">Sign up</div>
  <div class="search">
    <svg width="14" height="14" viewBox="0 0 14 14"><circle cx="5.5" cy="5.5" r="4.3" fill="none" stroke="#111" stroke-width="1.8"/><line x1="8.6" y1="8.6" x2="13" y2="13" stroke="#111" stroke-width="2"/></svg>
    <span>Search projects ...</span>
  </div>
</header>

<section class="hero">
  <div class="hero-art" role="img" aria-label="Silver world map with a light bulb rising above it and small figures around"></div>
  <h1 class="hero-title">Where the crowd meets great ideas!</h1>
  <div class="hero-rule"></div>
  <div class="hero-copy">
    <p>Raise money online for a cause and create personal<br>fundraisers for charity. LumoPledge is an innovative,<br>cost-effective online fundraising website for individual<br>fundraisers, non-profit fundraising and event fundraising.</p>
    <p>Raise money online for charity and have the most fun in<br>the world while doing it.</p>
  </div>
  <div class="btn btn-learn">learn more</div>
</section>

<aside class="sidebar">
  <div class="side-head popular">
    <svg width="12" height="14" viewBox="0 0 12 14"><path d="M6 3C2 3 1 7 2 10s3 4 4 3c1 1 3 0 4-3s0-7-4-7z" fill="#7ab51d"/><path d="M6 3l1-3" stroke="#7ab51d" stroke-width="1.4"/></svg>
    <span>Popular</span>
  </div>
  <div class="side-head featured">
    <svg width="14" height="14" viewBox="0 0 14 14"><path d="M7 0l2 4.6 5 .5-3.8 3.3 1.1 4.9L7 10.8 2.7 13.3l1.1-4.9L0 5.1l5-.5z" fill="#f07d1a"/></svg>
    <span>Featured</span>
  </div>
  <div class="side-head categories">
    <svg width="14" height="14" viewBox="0 0 14 14"><rect x="0.5" y="0.5" width="8" height="8" fill="none" stroke="#21799f"/><rect x="5.5" y="5.5" width="8" height="8" fill="#fff" stroke="#21799f"/></svg>
    <span>Categories</span>
  </div>
  <ul class="cat-list">
    <li>Art</li><li>Comics</li><li>Dance</li><li>Design</li><li>Fashion</li><li>Film &amp; Video</li><li>Food</li><li>Games</li><li>Music</li><li>Photography</li><li>Publishing</li><li>Technology</li><li>Theater</li>
  </ul>
</aside>

<main class="projects">
  <article class="card" style="left:6px">
    <div class="card-icon"></div>
    <div class="card-title">The Flarecast</div>
    <div class="card-by">by Tindel and Moss Lab</div>
    <div class="card-photo" role="img" aria-label="Project photo: metal torch attachment with a wire cage"></div>
    <p class="card-desc">Turns a blowtorch into a hand-held<br>supercharged instant-power broiler.<br>Sears fish, sous-vide, pizza, cheese,<br>foie, and everything</p>
    <svg class="card-pin" width="13" height="19" viewBox="0 0 13 19"><path d="M6.5 0A6.5 6.5 0 0 0 0 6.5C0 11 6.5 19 6.5 19S13 11 13 6.5A6.5 6.5 0 0 0 6.5 0z" fill="#222"/><circle cx="6.5" cy="6.5" r="2.5" fill="#fff"/></svg>
    <div class="card-loc">New York, NY</div>
    <div class="progress"><div class="progress-track"><div class="progress-fill"></div></div></div>
    <div class="stat stat-funded"><b>74%</b><span>funded</span></div>
    <div class="stat stat-pledged"><b>$59,205</b><span>pledged</span></div>
    <div class="stat stat-days"><b>25</b><span>days to go</span></div>
  </article>
  <article class="card" style="left:222px">
    <div class="card-icon"></div>
    <div class="card-title">The Flarecast</div>
    <div class="card-by">by Tindel and Moss Lab</div>
    <div class="card-photo" role="img" aria-label="Project photo: metal torch attachment with a wire cage"></div>
    <p class="card-desc">Turns a blowtorch into a hand-held<br>supercharged instant-power broiler.<br>Sears fish, sous-vide, pizza, cheese,<br>foie, and everything</p>
    <svg class="card-pin" width="13" height="19" viewBox="0 0 13 19"><path d="M6.5 0A6.5 6.5 0 0 0 0 6.5C0 11 6.5 19 6.5 19S13 11 13 6.5A6.5 6.5 0 0 0 6.5 0z" fill="#222"/><circle cx="6.5" cy="6.5" r="2.5" fill="#fff"/></svg>
    <div class="card-loc">New York, NY</div>
    <div class="progress"><div class="progress-track"><div class="progress-fill"></div></div></div>
    <div class="stat stat-funded"><b>74%</b><span>funded</span></div>
    <div class="stat stat-pledged"><b>$59,205</b><span>pledged</span></div>
    <div class="stat stat-days"><b>25</b><span>days to go</span></div>
  </article>
  <article class="card" style="left:438px">
    <div class="card-icon"></div>
    <div class="card-title">The Flarecast</div>
    <div class="card-by">by Tindel and Moss Lab</div>
    <div class="card-photo" role="img" aria-label="Project photo: metal torch attachment with a wire cage"></div>
    <p class="card-desc">Turns a blowtorch into a hand-held<br>supercharged instant-power broiler.<br>Sears fish, sous-vide, pizza, cheese,<br>foie, and everything</p>
    <svg class="card-pin" width="13" height="19" viewBox="0 0 13 19"><path d="M6.5 0A6.5 6.5 0 0 0 0 6.5C0 11 6.5 19 6.5 19S13 11 13 6.5A6.5 6.5 0 0 0 6.5 0z" fill="#222"/><circle cx="6.5" cy="6.5" r="2.5" fill="#fff"/></svg>
    <div class="card-loc">New York, NY</div>
    <div class="progress"><div class="progress-track"><div class="progress-fill"></div></div></div>
    <div class="stat stat-funded"><b>74%</b><span>funded</span></div>
    <div class="stat stat-pledged"><b>$59,205</b><span>pledged</span></div>
    <div class="stat stat-days"><b>25</b><span>days to go</span></div>
  </article>
</main>

<footer class="site-footer">
  <i>|</i><a>Discover</a><i>|</i><a>Start</a><i>|</i><a>How it works</a><i>|</i><a>Popular</a><i>|</i><a>Featured</a><i>|</i><a>Categories</a><i>|</i><a>Log in</a><i>|</i><a>Sing up</a><i>|</i>
</footer>

</body>
</html>
```